MEKO Business Card Design

I have a rough idea of the design / layout of the company business card but need help in finalizing the design and quality.

I'm looking for the card to be stand out, but simple, on the front with clear detail on the back with space for some one to write any other detail they need onto the card. The rough draft includes the crinkled graph paper back ground which I quite like for the front.

I will need the card design completed and ready to print in Australian business card standard sizes. This includes detail on all colors, fonts and type faces used as well as copy of the original for editing (inserting other employee details).

I have included the company logo and a rough draft of the card, including the graphic I would like to use for the back ground on the front, I am not sure that the graphic is any good for printing, not the highest res.

Thanks,

Lyle

```html
<!DOCTYPE html>
<html lang="en">
<head>
<meta charset="utf-8">
<title>MEKO Business Card</title>
<link href="https://fonts.googleapis.com/css2?family=Roboto:wght@400;500;700&display=swap" rel="stylesheet">
<style>
  :root {
    --page-bg: #e9e9e9;
    --card-white: #ffffff;
    --card-shade: #ececec;
    --band-black: #111111;
    --swoosh-grey: #9a9a9a;
    --swoosh-light: #cfcfcf;
    --ink: #1c1c1c;
    --ink-soft: #3a3a3a;
    --name-white: #ffffff;
  }
  html, body {
    margin: 0;
    width: 1200px;
    height: 899px;
    overflow: hidden;
    background: var(--page-bg);
    font-family: "Roboto", Arial, sans-serif;
  }
  .canvas {
    position: relative;
    width: 1200px;
    height: 899px;
  }
  .card {
    position: absolute;
    left: 150px;
    top: 175px;
    width: 900px;
    height: 550px;
    border-radius: 60px;
    overflow: hidden;
    background: linear-gradient(160deg, var(--card-white) 40%, var(--card-shade) 100%);
    box-shadow: 0 8px 24px rgba(0,0,0,0.18);
  }
  .card-art {
    position: absolute;
    inset: 0;
  }
  .holder-name {
    position: absolute;
    left: 58px;
    top: 44px;
    margin: 0;
    color: var(--name-white);
    font-size: 34px;
    font-weight: 500;
    letter-spacing: 2px;
    text-transform: uppercase;
    white-space: nowrap;
  }
  .holder-role {
    position: absolute;
    left: 58px;
    top: 88px;
    margin: 0;
    color: var(--name-white);
    font-size: 20px;
    font-weight: 400;
    letter-spacing: 2px;
    text-transform: uppercase;
    white-space: nowrap;
  }
  .address {
    position: absolute;
    left: 58px;
    top: 222px;
    margin: 0;
    color: var(--ink);
    font-size: 17px;
    line-height: 22px;
  }
  .contact-list {
    position: absolute;
    left: 40px;
    top: 290px;
    margin: 0;
    padding: 0;
    list-style: none;
  }
  .contact-list li {
    display: flex;
    align-items: center;
    height: 28px;
    color: var(--ink-soft);
    font-size: 15px;
    letter-spacing: 0.5px;
    white-space: nowrap;
  }
  .contact-list svg {
    width: 16px;
    height: 16px;
    margin-right: 12px;
    fill: var(--ink-soft);
  }
  .brand-name {
    position: absolute;
    left: 360px;
    top: 270px;
    margin: 0;
    color: var(--ink);
    font-size: 124px;
    font-weight: 700;
    line-height: 1;
    letter-spacing: 2px;
    white-space: nowrap;
  }
</style>
</head>
<body>
<div class="canvas">
  <div class="card">
    <svg class="card-art" viewBox="0 0 900 550" width="900" height="550" aria-hidden="true">
      <path class="swoosh swoosh-outer" d="M0,200 C140,150 260,150 390,162 C590,180 700,90 900,70 V84 C700,104 600,196 390,178 C260,168 140,170 0,214 Z" fill="var(--swoosh-light)"/>
      <path class="swoosh swoosh-mid" d="M0,188 C140,140 260,140 390,152 C590,170 700,80 900,58 V72 C700,92 600,184 390,166 C260,156 140,158 0,202 Z" fill="var(--swoosh-grey)"/>
      <path class="top-band" d="M0,0 H900 V50 C700,68 600,162 390,144 C260,132 140,132 0,182 Z" fill="var(--band-black)"/>
    </svg>

    <h1 class="holder-name">Daniel Carver</h1>
    <p class="holder-role">Financial Advisor</p>

    <p class="address">41 Level 9 Harbour Crest<br>Lane Bay</p>

    <ul class="contact-list">
      <li>
        <svg viewBox="0 0 16 16"><path d="M4 1h3l1 4-2 1c1 2 2 3 4 4l1-2 4 1v3c0 1-1 2-2 2C6 14 2 10 2 3c0-1 1-2 2-2z"/></svg>
        021 555 0147
      </li>
      <li>
        <svg viewBox="0 0 16 16"><path d="M4 0h8a1 1 0 0 1 1 1v14a1 1 0 0 1-1 1H4a1 1 0 0 1-1-1V1a1 1 0 0 1 1-1zm1 2v10h6V2zm3 11a1 1 0 1 0 0 2 1 1 0 0 0 0-2z"/></svg>
        021 555 0147
      </li>
      <li>
        <svg viewBox="0 0 16 16"><path d="M4 1h8v4H4zM1 6h14v7h-3v2H4v-2H1zm4 4v4h6v-4z"/></svg>
        021 555 0147
      </li>
      <li>
        <svg viewBox="0 0 16 16"><path d="M1 3h14v10H1zm1 1v1l6 4 6-4V4z"/></svg>
        hello@mekoav.au
      </li>
      <li>
        <svg viewBox="0 0 16 16"><path d="M8 1a7 7 0 1 0 0 14A7 7 0 0 0 8 1zm0 1.5c.8 0 1.8 1.6 2.1 4.5H5.9C6.2 4.1 7.2 2.5 8 2.5zM5.9 9h4.2c-.3 2.9-1.3 4.5-2.1 4.5S6.2 11.9 5.9 9z"/></svg>
        www.mekoav.com.au
      </li>
    </ul>

    <p class="brand-name">MEKO</p>
  </div>
</div>
</body>
</html>
```